Website visual upgrade

I am seeking expressions of interest for the updating the visuals of my website www.lunvaleplacements.example
I am basically seeking a simple,bold and visually strong graphic makeover.using existing or shortly to be modified text.

```html
<!DOCTYPE html>
<html lang="en">
<head>
<meta charset="utf-8">
<title>Lunvale Placements — Who we are</title>
<link rel="stylesheet" href="https://fonts.googleapis.com/css2?family=Arimo:ital,wght@0,400;0,700;1,400&display=swap">
<style>
  :root {
    --sky-top: #3f4038;
    --sky-mid: #6b5a44;
    --rock-glow: #c8733e;
    --rock-deep: #7a3a22;
    --cloud: #b86a40;
    --sidebar: rgba(8, 8, 8, 0.93);
    --panel: rgba(10, 8, 8, 0.86);
    --accent: #d0162a;
    --text: #ffffff;
    --text-soft: #e8e8e8;
    --photo-worker: #7c6a58;
    --photo-city: #4a7fb8;
    --scroll: #3a3a3a;
  }
  * { box-sizing: border-box; margin: 0; padding: 0; }
  html, body { width: 1200px; height: 602px; overflow: hidden; }
  body {
    position: relative;
    font-family: "Arimo", Arial, sans-serif;
    color: var(--text);
    background: #000;
  }
  .backdrop {
    position: absolute; inset: 0;
    background:
      radial-gradient(ellipse 40% 30% at 10% 40%, rgba(230,140,80,.55), transparent 70%),
      radial-gradient(ellipse 35% 30% at 90% 55%, rgba(230,140,80,.6), transparent 70%),
      linear-gradient(180deg, var(--sky-top) 0%, var(--sky-mid) 22%, var(--rock-deep) 45%, var(--rock-glow) 62%, var(--rock-deep) 78%, var(--cloud) 100%);
  }
  .sidebar {
    position: absolute; left: 116px; top: 0;
    width: 245px; height: 602px;
    background: var(--sidebar);
  }
  .brand {
    position: absolute; left: 24px; top: 38px;
    display: flex; align-items: center; gap: 10px;
    font-size: 21px; font-weight: 400; color: var(--text);
    white-space: nowrap;
  }
  .brand-dot {
    width: 18px; height: 18px; border-radius: 50%;
    background: var(--accent);
  }
  .main-nav {
    position: absolute; right: 31px; top: 183px;
    list-style: none; text-align: right;
  }
  .main-nav li {
    font-size: 11.5px; font-weight: 700;
    line-height: 27px; color: var(--text);
  }
  .main-nav li.is-current { color: var(--accent); font-weight: 400; }
  .content-panel {
    position: absolute; left: 416px; top: 121px;
    width: 587px; height: 386px;
    background: var(--panel);
  }
  .section-title {
    position: absolute;
    font-size: 15px; font-style: italic; color: var(--accent);
  }
  .section-rule {
    position: absolute; height: 1px;
    background: var(--accent); opacity: .75;
  }
  .photo {
    position: absolute; width: 72px; height: 68px;
    border: 1px solid #b05a40;
  }
  .photo--worker { background: linear-gradient(160deg, #8a8f93, var(--photo-worker) 55%, #3c3630); }
  .photo--city { background: linear-gradient(180deg, var(--photo-city), #9ab8d8 55%, #3d4a3a); }
  .copy {
    position: absolute; left: 105px; width: 440px;
    font-size: 10.5px; line-height: 18px; color: var(--text-soft);
  }
  .copy p + p { margin-top: 18px; }
  .scrollbar {
    position: absolute; left: 573px; top: 26px;
    width: 3px; height: 318px;
    background: var(--scroll); border-radius: 2px;
  }
  .site-footer {
    position: absolute; left: 594px; top: 577px;
    font-size: 10.5px; font-weight: 700; color: var(--text);
    white-space: nowrap;
  }
</style>
</head>
<body>
  <div class="backdrop" role="img" aria-label="Photograph of snow-covered mountain peaks glowing orange above clouds at dusk, with a pale moon in the sky"></div>

  <aside class="sidebar">
    <div class="brand"><span class="brand-dot"></span>Lunvale Placements</div>
    <ul class="main-nav">
      <li>Home</li>
      <li class="is-current">Who we are</li>
      <li>Our Approach</li>
      <li>What We Do</li>
      <li>Migration Assistance</li>
      <li>Job Seeker</li>
      <li>Useful Links</li>
      <li>Support</li>
      <li>Contact&nbsp; Use</li>
    </ul>
  </aside>

  <main class="content-panel">
    <h2 class="section-title" style="left:17px; top:20px;">About Us</h2>
    <div class="section-rule" style="left:104px; top:30px; width:428px;"></div>
    <div class="photo photo--worker" role="img" aria-label="Photo of a construction worker in a white hard hat on a building site" style="left:17px; top:51px;"></div>
    <div class="copy" style="top:46px;">
      <p>We are committed to providing the highest standards<br>of service in Executive search and selection and the provision of Skilled trades people and allied Health professionals throughout Australia.</p>
      <p>We have offices throughout Australia, clearly adding<br>value to our clients’ strategic needs, wherever they may be.</p>
      <p>Competing organisations have access to similar Technology, Raw Materials and Human Capital. The ability to identify, attract and retain quality personnel will clearly differentiate those organisations which are successful and develop a corporate culture of excellence and innovation.</p>
    </div>

    <h2 class="section-title" style="left:14px; top:236px;">History</h2>
    <div class="section-rule" style="left:104px; top:245px; width:428px;"></div>
    <div class="photo photo--city" role="img" aria-label="Photo of city skyscrapers under a blue sky" style="left:17px; top:267px;"></div>
    <div class="copy" style="top:263px;">
      <p>Our firm is proudly 100% Australian owned and operated. We have excellent alliance partners in South Africa, The Philippines, New Zealand and the UK.</p>
      <p>We commenced operations in Melbourne in 1992 and have grown nationally with offices in Melbourne, Brisbane, Sydney and Perth.</p>
    </div>

    <div class="scrollbar"></div>
  </main>

  <footer class="site-footer">Privacy Policy | Site Map | © 2013. Lunvale Partner. All Rights Reserved.</footer>
</body>
</html>
```